Villa Serena needs a new website for its boutique apartment

We are a boutique apartment in Florence that rents out to tourists. We are looking to redesign our website. See the existing site at www.villaserena-stay.example

Ideally redesigned site would enable us to easily add and change photos in the gallery and across the site.

The new logo for the apartment is currently under design but being based around the current house logo with a person standing inside.
Updates

Reason: The website design by the 1st Place designer has been long and drawn out and not led to the design that we were looking for. As such, we are extending the deadline for another 5 days to hopefully get new designs and options.

Target Market(s)

Global tourists

Industry/Entity Type

Accommodation

Coding

Coded - Design and coding required

Number of Pages Required

5+ page

Font styles to use
Sans Serif

Requirements
Must have
• Welcome page, gallery page, information page about apartment and availability page with link to booking sites. And option for another page with tourist information. We must be able to change the photos in the gallery with relative ease when required.
• The Villa Serena font has been uploaded which is used with the logo and the new logo has been uploaded.
Nice to have
• Looking like a fun but professional hotel site
• Page info is located on www.villaserena-stay.example site

```html
<!DOCTYPE html>
<html lang="en">
<head>
<meta charset="utf-8">
<title>Villa Serena – Boutique Apartment in Florence</title>
<link rel="stylesheet" href="https://fonts.googleapis.com/css2?family=Open+Sans:wght@300;400;600&display=swap">
<style>
  :root {
    --orange: #f07324;
    --ink: #333333;
    --muted: #777777;
    --white: #ffffff;
    --band: #f4f4f4;
    --badge: #d9d9d9;
    --red: #d8404a;
    --strip: rgba(40, 40, 40, 0.72);
  }
  * { box-sizing: border-box; margin: 0; padding: 0; }
  html, body { width: 1200px; height: 2338px; overflow: hidden; }
  body { font-family: "Open Sans", Arial, sans-serif; color: var(--ink); background: var(--white); position: relative; }

  .site-header { position: absolute; top: 0; left: 0; width: 1200px; height: 97px; background: var(--white); }
  .brand { position: absolute; left: 140px; top: 30px; display: flex; align-items: center; gap: 10px; font-size: 17px; font-weight: 600; color: var(--ink); }
  .brand-mark { width: 14px; height: 14px; background: var(--ink); }
  .main-nav { position: absolute; right: 141px; top: 40px; display: flex; gap: 35px; }
  .main-nav a, .footer-nav a { font-size: 13px; font-weight: 600; color: var(--ink); text-decoration: none; text-transform: uppercase; }
  .main-nav a.active { color: var(--orange); }

  .hero { position: absolute; top: 97px; left: 0; width: 1200px; height: 587px; background: linear-gradient(135deg, #d8cfc2 0%, #c7b9a6 40%, #8a7a68 75%, #4e4136 100%); text-align: center; color: var(--white); }
  .hero-title { position: absolute; top: 222px; width: 100%; font-size: 40px; font-weight: 400; letter-spacing: 1px; }
  .hero-sub { position: absolute; top: 277px; width: 100%; font-size: 16px; }
  .btn { display: inline-block; background: var(--orange); color: var(--white); font-weight: 600; text-transform: uppercase; text-decoration: none; }
  .hero .btn { position: absolute; top: 333px; left: 533px; width: 131px; height: 40px; line-height: 40px; font-size: 13px; }
  .hero-dots { position: absolute; top: 535px; left: 584px; display: flex; gap: 10px; }
  .hero-dots span { width: 8px; height: 8px; border-radius: 50%; background: rgba(255,255,255,0.5); }
  .hero-dots span.on { background: var(--white); }

  .partners { position: absolute; top: 684px; left: 0; width: 1200px; height: 146px; background: var(--band); display: flex; justify-content: center; align-items: center; gap: 42px; }
  .partner-badge { width: 190px; height: 40px; border-radius: 6px; background: var(--badge); }

  .features { position: absolute; top: 830px; left: 0; width: 1200px; height: 312px; }
  .feature { position: absolute; top: 72px; width: 290px; }
  .feature-head { display: flex; align-items: center; gap: 14px; height: 56px; }
  .feature-head h3 { font-size: 15px; font-weight: 600; text-transform: uppercase; color: #555; }
  .feature p { margin-top: 26px; font-size: 11.5px; line-height: 26px; color: var(--muted); }

  .gallery { position: absolute; top: 1142px; left: 0; width: 1200px; height: 515px; background: linear-gradient(90deg, #b9b3a8 0%, #e2dcd1 35%, #d9d0c2 60%, #a89c8c 85%, #7f8a9a 100%); }
  .section-title { font-size: 30px; font-weight: 400; text-transform: uppercase; text-align: center; }
  .gallery .section-title { position: absolute; top: 76px; width: 100%; color: #2d2d2d; }
  .thumb-strip { position: absolute; top: 388px; left: 0; width: 1200px; height: 127px; background: var(--strip); }
  .thumb { position: absolute; top: 24px; width: 141px; height: 100px; }
  .thumb.current { border: 4px solid var(--white); }
  .strip-arrow { position: absolute; top: 46px; }

  .availability { position: absolute; top: 1657px; left: 0; width: 1200px; height: 376px; background: linear-gradient(180deg, #d8404a 0%, #d13a44 100%); color: var(--white); text-align: center; }
  .availability .section-title { position: absolute; top: 74px; width: 100%; }
  .availability p { position: absolute; top: 150px; width: 100%; font-size: 17px; line-height: 30px; }
  .availability .btn { position: absolute; top: 233px; left: 470px; width: 259px; height: 48px; line-height: 48px; font-size: 17px; font-weight: 400; }

  .site-footer { position: absolute; top: 2033px; left: 0; width: 1200px; height: 305px; text-align: center; }
  .site-footer .brand { position: absolute; left: 0; width: 100%; top: 95px; justify-content: center; font-size: 20px; }
  .footer-nav { position: absolute; top: 192px; width: 100%; display: flex; justify-content: center; gap: 35px; }
  .copyright { position: absolute; top: 229px; width: 100%; font-size: 13px; font-weight: 600; color: #444; }
</style>
</head>
<body>

<header class="site-header">
  <div class="brand"><span class="brand-mark"></span>Villa Serena</div>
  <nav class="main-nav">
    <a class="active" href="#">Home</a>
    <a href="#">About Us</a>
    <a href="#">Gallery</a>
    <a href="#">Info</a>
    <a href="#">Availability</a>
    <a href="#">Contact Us</a>
  </nav>
</header>

<section class="hero" role="img" aria-label="Bright living room with a cream sofa, tulips on a wooden table, a red bean bag and tall windows">
  <h1 class="hero-title">VILLA SERENA</h1>
  <p class="hero-sub">We are a boutique apartment that rents out to tourists</p>
  <a class="btn" href="#">Get Started</a>
  <div class="hero-dots"><span></span><span class="on"></span><span></span></div>
</section>

<section class="partners" aria-label="Listing partners">
  <div class="partner-badge"></div>
  <div class="partner-badge" style="width:150px"></div>
  <div class="partner-badge"></div>
  <div class="partner-badge" style="width:250px"></div>
</section>

<section class="features">
  <div class="feature" style="left:145px">
    <div class="feature-head">
      <svg width="56" height="56" viewBox="0 0 56 56" fill="none" stroke="#f07324" stroke-width="2">
        <rect x="6" y="6" width="40" height="44" rx="3"/>
        <path d="M14 16h24M14 24h24M14 32h14"/>
        <circle cx="44" cy="44" r="6"/>
      </svg>
      <h3>The Space</h3>
    </div>
    <p>A newly renovated boutique 2-bedroom loft apartment in the historic centre of Florence, offering luxury accommodation for up to six adults.</p>
  </div>
  <div class="feature" style="left:455px">
    <div class="feature-head">
      <svg width="56" height="56" viewBox="0 0 56 56" fill="none" stroke="#f07324" stroke-width="2">
        <rect x="8" y="6" width="36" height="44" rx="2"/>
        <path d="M18 30l8-7 8 7v10H18z"/>
        <path d="M46 20l6 6-14 14h-6v-6z"/>
      </svg>
      <h3>Furnishings</h3>
    </div>
    <p>Bedding available for your stay is a king-sized bed, queen-sized bed and a pull-out double-sized sofa bed. There are one and a half bathrooms</p>
  </div>
  <div class="feature" style="left:768px">
    <div class="feature-head">
      <svg width="56" height="56" viewBox="0 0 56 56" fill="none" stroke="#f07324" stroke-width="2">
        <circle cx="24" cy="24" r="17"/>
        <path d="M36 36l14 14"/>
        <path d="M16 26l8-7 8 7v8H16z"/>
      </svg>
      <h3>Getting Around</h3>
    </div>
    <p>Perfectly located for sightseeing - Via delle Rose is only a few minutes walk (600m) to the Ponte Vecchio, Duomo and Palazzo Vecchio.</p>
  </div>
</section>

<section class="gallery" role="img" aria-label="Loft corner with a wing chair, an arched floor lamp and a wooden console table">
  <h2 class="section-title">Gallery</h2>
  <div class="thumb-strip">
    <svg class="strip-arrow" style="left:90px" width="18" height="30" viewBox="0 0 18 30"><path d="M14 4L4 15l10 11" fill="none" stroke="#fff" stroke-width="4"/></svg>
    <div class="thumb current" role="img" aria-label="Chair and lamp" style="left:164px;background:#c8b89c"></div>
    <div class="thumb" role="img" aria-label="Bedroom" style="left:313px;background:#8d98a8"></div>
    <div class="thumb" role="img" aria-label="Bedroom with window" style="left:464px;background:#6e7c94"></div>
    <div class="thumb" role="img" aria-label="White bed" style="left:615px;background:#d9dbe0"></div>
    <div class="thumb" role="img" aria-label="Dining area" style="left:762px;background:#cdb7a4"></div>
    <div class="thumb" role="img" aria-label="Kitchen" style="left:915px;background:#8b6f66"></div>
    <svg class="strip-arrow" style="left:1112px" width="18" height="30" viewBox="0 0 18 30"><path d="M4 4l10 11L4 26" fill="none" stroke="#fff" stroke-width="4"/></svg>
  </div>
</section>

<section class="availability" role="img" aria-label="Red-tinted view of the living room with sofa and radiator">
  <h2 class="section-title">Availability</h2>
  <p>Please find our up to date Availability below.<br>Click on the link at the bottom or on our Contact page to make a reservation:</p>
  <a class="btn" href="#">Check the Availability</a>
</section>

<footer class="site-footer">
  <div class="brand"><span class="brand-mark"></span>Villa Serena</div>
  <nav class="footer-nav">
    <a href="#">Home</a>
    <a href="#">About Us</a>
    <a href="#">Gallery</a>
    <a href="#">Info</a>
    <a href="#">Availability</a>
    <a href="#">Contact Us</a>
  </nav>
  <p class="copyright">© 2016 COMPANY NAME &nbsp;|&nbsp; ALL RIGHTS RESERVED</p>
</footer>

</body>
</html>
```